BrambleShore.com Web Site Theme - Home Page/Front Page - Sub-Page theme

Looking for a new site theme that uses tiles like Plinkerdaily.com but with a unique style. Topbar categories should include following in any particular order w/ pop-out at touch w/ sub-categories (examples below): The main categories for display have an >> prefix . Note main catgories and sub-categories may change.

SPECIAL NOTE: Regional site. We need a way to navigate/drill-down to specific regions on the Bramble Shore (see the cities accross the top on the current site design)

PORTAL SITE: This site will have a back-end w/ my account and therefore may use a Scaffolix template on the back-end for managing Tiles and articles. Tiles would be the organic content/advertisements on the home page that link to the sub-pages.

TOP BAR CATEGORIES - click to open pop-up w/ sub-categories (some examples in Dining and Real Estate below)

>>Lodging

>>Dining (sub categories below)
Go to Dining >>
Bars & Nightclubs
Lunch & Dinner
Catering
Chinese
Coffee
Italian
Pizza
Seafood
Steakhouse
More >>

>>Wineries

>>Activities & Events

>>Real Estate

>>For Sale (subcategories below)
Auto
Shopping

>>Jobs
..

Target Market(s)

Hotels, Wineries, Restaurants, Tourists

Industry/Entity Type

Real Estate

Coding

Coded - Design and coding required

Number of Pages Required

3 page

Colors
0255a3

Requirements
Must have
• My account (maybe a black bar w/ BS logo accross top w/ My Account, Settings, Login etc)
• Conversion of existing organic content and advertisements to new Tiles platform.
Nice to have
• Kind of a Hybrid between Zorv.com and PlinkerDaily.com
• PORTAL THOUGHTS
• If everything were to be thought of as a tile to preview in a 3 column wide format w/ variable heights you can fit articles and sound content mixed in with advertorials.
• Every square tile on BrambleShore.com could be encapsulated into a “Tile”. The Tile is the preview of the landing page, article, or page.
• Every article, business listings, google map page, etc. can have a Tile associated with it. OR you create a Tile and link it to a URL/page.
• So Tiles become mini snippets of custom HTML that can have 1 or more links etc… Just an HTML Snippet.
• Tile/HTML Snippet
• PreviewTiles.aspx
• Shows all tiles sortable like a product catalog, etc. Additional columns for publishing the tile and where it should reside on the Front Page?
• NEW THEME
• Removal of the traditional BS sidebar and incorporating the triple tile site design. We can still have Fernmarsh or a major display as first thing you see above top-bar. The categories can be incorporated into a simple top-bar that on-click you pop-down all subcategories and anything featured. This supports tablets and handhelds instead of the traditional mouse-over...
• Comp Layout (see plinkerdaily.com)
• 3 columns to 1 column style?
• How to handle mobile devices? (Tiles technique supports Quibbit news mobile app - 3 columns PC/Mac browser - 1 column Mobile Phone
• Tile & Page MGT
• How do we convert the existing content pages to our new Tile/Page technique?
• How do we handle advertising Tiles and Tiles embedded on pages?
• Pages
• How is a page handled?
• How are Tiles managed and is that a Page or not?
• How are listings handled and are they defined as a Page?

```html
<!DOCTYPE html>
<html lang="en">
<head>
<meta charset="utf-8">
<title>BrambleShore.com – Home</title>
<link rel="stylesheet" href="https://fonts.googleapis.com/css2?family=Montserrat:wght@400;600;700;800&family=Open+Sans:wght@400;600;700&display=swap">
<style>
:root{
  --brand:#0255a3;
  --brand-light:#1a73c9;
  --brand-dark:#013f7c;
  --navy:#0d2a4f;
  --ink:#222;
  --rule:#dcdcdc;
  --black:#0a0a0a;
  --white:#fff;
  --page:#fff;
}
*{box-sizing:border-box;margin:0;padding:0}
html,body{width:1200px;height:4945px;overflow:hidden}
body{position:relative;background:var(--page);font-family:"Open Sans",Arial,sans-serif;color:var(--ink)}
.abs{position:absolute}

/* utility bar */
.utility-bar{top:0;left:0;width:1200px;height:26px;background:var(--black);display:flex;align-items:center;justify-content:space-between;padding:0 18px;font-size:9px;color:#9a9a9a}
.region-links{display:flex;gap:16px}
.account-links{display:flex;gap:16px;color:#ddd;font-weight:600}
.account-links span::before{content:"";display:inline-block;width:7px;height:7px;border-radius:50%;background:#bbb;margin-right:5px;vertical-align:-1px}

/* masthead */
.masthead{top:26px;left:0;width:1200px;height:74px;background:var(--black);display:flex;align-items:center;justify-content:center}
.logo{font-family:"Montserrat",sans-serif;font-weight:800;font-size:34px;color:var(--white);letter-spacing:-.5px}

/* main nav */
.main-nav{top:100px;left:0;width:1200px;height:65px;background:linear-gradient(var(--brand-light),var(--brand))}
.main-nav ul{list-style:none;display:flex;justify-content:space-between;width:970px;margin:0 auto;height:65px;padding:0 8px}
.main-nav li{font-family:"Montserrat",sans-serif;font-weight:700;font-size:14px;color:var(--white);display:flex;align-items:center;padding:0 14px}
.main-nav li.is-open{background:var(--brand-dark)}

/* hero */
.hero{top:165px;left:115px;width:970px;height:530px;background:radial-gradient(ellipse at 55% 25%,#f2c98a 0%,#b1763b 18%,#4b2a17 45%,#150c08 80%);box-shadow:0 22px 24px -18px rgba(0,0,0,.55)}
.hero-search{top:420px;left:115px;width:745px;height:56px;display:flex}
.hero-search .field{flex:1;background:var(--white);display:flex;align-items:center;padding-left:22px;font-size:14px;color:#666}
.hero-search .btn{width:270px;background:var(--brand);color:var(--white);font-family:"Montserrat",sans-serif;font-weight:700;font-size:16px;display:flex;align-items:center;justify-content:center;letter-spacing:1px}
.hero-dots{top:485px;left:0;width:970px;display:flex;justify-content:center;gap:9px}
.hero-dots i{width:8px;height:8px;border-radius:50%;background:rgba(255,255,255,.5)}
.hero-dots i.on{background:var(--white)}

/* dropdowns */
.dropdown{background:var(--white);box-shadow:0 4px 10px rgba(0,0,0,.25);padding:16px 18px;font-size:12px;color:#333}
.dropdown li{list-style:none;line-height:25px}
.dropdown li::before{content:"›";color:var(--brand);margin-right:8px}
.dropdown li.more{color:var(--brand);font-weight:700}
.dropdown li.more::before{content:""}
.dining-menu{top:165px;left:225px;width:172px}
.forsale-menu{top:165px;left:733px;width:92px;padding:10px 14px}

/* section headings */
.section-title{font-family:"Montserrat",sans-serif;font-weight:700;font-size:20px;color:var(--brand)}
.featured-heading{top:776px;left:0;width:1200px;text-align:center}

/* category tiles */
.category-tile{top:840px;width:306px;height:405px}
.category-tile .photo{height:200px}
.category-tile ul{background:var(--brand);height:205px;list-style:none;padding:34px 26px;color:var(--white);font-size:14px;line-height:32px}
.category-tile li::before{content:"›";margin-right:12px;font-weight:700}

/* blog */
.blog-heading{top:1325px;left:115px}
.blog-grid{top:1392px;left:115px;width:637px;display:grid;grid-template-columns:306px 306px;column-gap:25px}
.post-card{height:557px;border-bottom:1px solid var(--rule);padding-top:10px}
.post-card h3{font-weight:700;font-size:14px;line-height:18px;color:var(--navy);height:40px}
.post-card .photo{height:210px;margin-top:10px}
.post-card p{font-size:12.5px;line-height:19px;color:#333;margin-top:16px;height:152px}
.post-meta{display:flex;align-items:center;gap:8px;font-size:11px;color:#333;margin-top:24px}
.post-meta svg{width:14px;height:14px;fill:#333}
.post-meta .spacer{width:12px}
.read-more{margin-left:auto;background:var(--brand);color:var(--white);font-weight:700;font-size:10px;padding:7px 14px;border-radius:2px}

/* pagination */
.pagination{top:4752px;left:115px;width:637px;display:flex;justify-content:center;gap:6px}
.pagination span{min-width:26px;height:26px;border:1px solid #ccc;font-size:11px;display:flex;align-items:center;justify-content:center;color:#444;padding:0 5px}
.pagination span.on{background:var(--brand);border-color:var(--brand);color:var(--white)}

/* sidebar */
.side-label{font-size:10px;font-weight:600;color:#888;letter-spacing:.5px;left:782px}
.sponsor-slot{left:782px;width:303px}
.sponsor-tall{top:1362px;height:653px;background:linear-gradient(180deg,#6f9fb7 0%,#8fb0a8 40%,#5f6d3e 75%,#3d4a24 100%)}
.sponsor-wide{top:3390px;height:240px;background:linear-gradient(120deg,#0c0c0c 50%,#3a2a1a 100%)}
.recent-heading{top:2068px;left:782px}
.recent-post{left:782px;width:303px;height:265px}
.recent-post .photo{height:210px}
.recent-post p{font-size:11px;color:#333;margin-top:7px}
.recent-post .post-meta{justify-content:flex-end;margin-top:8px;gap:6px}

.newsletter{top:2960px;left:782px;width:303px;height:275px;background:var(--brand);color:var(--white);padding:22px 22px}
.newsletter h4{font-family:"Montserrat",sans-serif;font-weight:700;font-size:42px;line-height:42px}
.newsletter h5{font-family:"Montserrat",sans-serif;font-weight:400;font-size:22px;line-height:26px}
.newsletter p{font-size:12px;line-height:17px;margin-top:12px}
.newsletter .email{margin-top:12px;height:32px;background:var(--brand-light);border:1px solid rgba(255,255,255,.4);font-size:11px;padding:8px 10px;color:#dbe8f6}
.newsletter .subscribe{display:inline-block;margin-top:10px;background:var(--navy);font-weight:700;font-size:11px;padding:8px 14px}
.newsletter small{display:block;margin-top:8px;font-size:9px;opacity:.85}
.social-row{top:3282px;left:782px;display:flex;gap:9px}
.social-row i{width:34px;height:34px;border-radius:50%;border:2px solid var(--brand);display:block}

/* footer */
.site-footer{top:4835px;left:0;width:1200px;height:110px;background:var(--black);color:var(--white);text-align:center;padding-top:30px}
.site-footer nav{display:flex;justify-content:center;gap:14px;font-family:"Montserrat",sans-serif;font-weight:600;font-size:12px}
.site-footer nav span+span::before{content:"|";margin-right:14px;color:#777}
.site-footer .copy{font-size:10px;margin-top:18px;color:#ccc}
.site-footer .mark{position:absolute;right:22px;top:52px;font-size:11px;font-weight:700;color:#888}
</style>
</head>
<body>

<div class="abs utility-bar">
  <div class="region-links"><span>Home</span><span>Santa Barbara</span><span>Pismo Beach</span><span>Avila Beach</span><span>Morro Bay</span><span>San Luis Obispo</span><span>Paso Robles</span><span>Monterey</span><span>San Clemente</span><span>Cambria</span></div>
  <div class="account-links"><span>My Account</span><span>Settings</span><span>Login</span></div>
</div>

<header class="abs masthead"><div class="logo">BrambleShore.com</div></header>

<nav class="abs main-nav">
  <ul>
    <li>LODGING</li><li class="is-open">DINING</li><li>WINERIES</li><li>ACTIVITIES &amp; EVENTS</li><li>REAL ESTATE</li><li class="is-open">FOR SALE</li><li>AUTO</li><li>SHOPPING</li><li>JOBS</li>
  </ul>
</nav>

<section class="abs hero" role="img" aria-label="Concert crowd with raised hands under warm stage lights">
  <div class="abs hero-search"><div class="field">Search For Bramble Shore</div><div class="btn">SEARCH</div></div>
  <div class="abs hero-dots"><i></i><i></i><i class="on"></i><i></i><i></i></div>
</section>

<ul class="abs dropdown dining-menu">
  <li>Bars &amp; Nightclubs</li><li>Lunch &amp; Dinner</li><li>Catering</li><li>Chinese</li><li>Coffee</li><li>Italian</li><li>Pizza</li><li>Seafood</li><li>Steakhouse</li><li class="more">More &gt;&gt;</li>
</ul>
<ul class="abs dropdown forsale-menu"><li>Auto</li><li>Shopping</li></ul>

<h2 class="abs section-title featured-heading">FEATURED CATEGORIES</h2>

<div class="abs category-tile" style="left:115px">
  <div class="photo" role="img" aria-label="Dinosaur statue silhouetted against an orange sunset" style="background:linear-gradient(#f0a040,#c8601c 60%,#3a2410)"></div>
  <ul><li>Butterfly Park</li><li>Dinosaur Caves</li><li>Walk the Pier</li><li>Fly a Kite</li></ul>
</div>
<div class="abs category-tile" style="left:445px">
  <div class="photo" role="img" aria-label="White speedboat on deep blue water seen from above" style="background:linear-gradient(135deg,#0f3a66,#1c5d92 50%,#0b2c4d)"></div>
  <ul><li>Kayaking</li><li>Boating</li><li>Surfing</li><li>Gardens</li></ul>
</div>
<div class="abs category-tile" style="left:782px">
  <div class="photo" role="img" aria-label="Golfer on a green course at sunrise" style="background:linear-gradient(#f3d27a,#b9b04a 45%,#4f7a28)"></div>
  <ul><li>Golf</li><li>Festivals</li><li>Lakes</li><li>Montana de Oro</li></ul>
</div>

<h2 class="abs section-title blog-heading">FEATURED BLOG POSTS</h2>

<div class="abs blog-grid">
  <article class="post-card"><h3>Traveling California's Bramble Shore<br>5 Reasons to Move to the West Coast</h3><div class="photo" role="img" aria-label="Bar shelves with bottles and glasses" style="background:linear-gradient(#d9cbb5,#7a5a3c)"></div><p>Lorem Ipsum is simply dummy text of the printing and typesetting industry. Lorem Ipsum has been the industry's standard dummy text ever since the 1500s, when an unknown printer took a galley of type and scrambled it to make a type specimen book. It has survived not only five centuries, but also the leap into electronic typesetting, remaining essentially unchanged.</p><div class="post-meta"><svg viewBox="0 0 16 16"><path d="M2 2h12v9H6l-4 3z"/></svg>Comments<span class="spacer"></span><svg viewBox="0 0 16 16"><circle cx="12" cy="3" r="2.5"/><circle cx="4" cy="8" r="2.5"/><circle cx="12" cy="13" r="2.5"/><path d="M4 8l8-5M4 8l8 5" stroke="#333" stroke-width="1.3"/></svg>Share<span class="read-more">Read More</span></div></article>
  <article class="post-card"><h3>Traveling California's Bramble Shore<br>5 Reasons to Move to the West Coast</h3><div class="photo" role="img" aria-label="Crowd at a night concert with purple stage lights" style="background:linear-gradient(#b08ad0,#4a1e5a 60%,#1a0a1e)"></div><p>Lorem Ipsum is simply dummy text of the printing and typesetting industry. Lorem Ipsum has been the industry's standard dummy text ever since the 1500s, when an unknown printer took a galley of type and scrambled it to make a type specimen book. It has survived not only five centuries, but also the leap into electronic typesetting, remaining essentially unchanged.</p><div class="post-meta"><svg viewBox="0 0 16 16"><path d="M2 2h12v9H6l-4 3z"/></svg>Comments<span class="spacer"></span><svg viewBox="0 0 16 16"><circle cx="12" cy="3" r="2.5"/><circle cx="4" cy="8" r="2.5"/><circle cx="12" cy="13" r="2.5"/><path d="M4 8l8-5M4 8l8 5" stroke="#333" stroke-width="1.3"/></svg>Share<span class="read-more">Read More</span></div></article>
  <article class="post-card"><h3>Traveling California's Bramble Shore<br>5 Reasons to Move to the West Coast</h3><div class="photo" role="img" aria-label="Conference hall with seated audience" style="background:linear-gradient(#c8dcec,#6c8aa6 60%,#3a4a5a)"></div><p>Lorem Ipsum is simply dummy text of the printing and typesetting industry. Lorem Ipsum has been the industry's standard dummy text ever since the 1500s, when an unknown printer took a galley of type and scrambled it to make a type specimen book. It has survived not only five centuries, but also the leap into electronic typesetting, remaining essentially unchanged.</p><div class="post-meta"><svg viewBox="0 0 16 16"><path d="M2 2h12v9H6l-4 3z"/></svg>Comments<span class="spacer"></span><svg viewBox="0 0 16 16"><circle cx="12" cy="3" r="2.5"/><circle cx="4" cy="8" r="2.5"/><circle cx="12" cy="13" r="2.5"/><path d="M4 8l8-5M4 8l8 5" stroke="#333" stroke-width="1.3"/></svg>Share<span class="read-more">Read More</span></div></article>
  <article class="post-card"><h3>Traveling California's Bramble Shore<br>5 Reasons to Move to the West Coast</h3><div class="photo" role="img" aria-label="Runners in a race on a green park road" style="background:linear-gradient(#e6ebe0,#8fb66a 55%,#4d7a2c)"></div><p>Lorem Ipsum is simply dummy text of the printing and typesetting industry. Lorem Ipsum has been the industry's standard dummy text ever since the 1500s, when an unknown printer took a galley of type and scrambled it to make a type specimen book. It has survived not only five centuries, but also the leap into electronic typesetting, remaining essentially unchanged.</p><div class="post-meta"><svg viewBox="0 0 16 16"><path d="M2 2h12v9H6l-4 3z"/></svg>Comments<span class="spacer"></span><svg viewBox="0 0 16 16"><circle cx="12" cy="3" r="2.5"/><circle cx="4" cy="8" r="2.5"/><circle cx="12" cy="13" r="2.5"/><path d="M4 8l8-5M4 8l8 5" stroke="#333" stroke-width="1.3"/></svg>Share<span class="read-more">Read More</span></div></article>
  <article class="post-card"><h3>Traveling California's Bramble Shore<br>5 Reasons to Move to the West Coast</h3><div class="photo" role="img" aria-label="Banquet table lit with violet lights" style="background:linear-gradient(#d06ad8,#5a1a7a 55%,#1e0a2a)"></div><p>Lorem Ipsum is simply dummy text of the printing and typesetting industry. Lorem Ipsum has been the industry's standard dummy text ever since the 1500s, when an unknown printer took a galley of type and scrambled it to make a type specimen book. It has survived not only five centuries, but also the leap into electronic typesetting, remaining essentially unchanged.</p><div class="post-meta"><svg viewBox="0 0 16 16"><path d="M2 2h12v9H6l-4 3z"/></svg>Comments<span class="spacer"></span><svg viewBox="0 0 16 16"><circle cx="12" cy="3" r="2.5"/><circle cx="4" cy="8" r="2.5"/><circle cx="12" cy="13" r="2.5"/><path d="M4 8l8-5M4 8l8 5" stroke="#333" stroke-width="1.3"/></svg>Share<span class="read-more">Read More</span></div></article>
  <article class="post-card"><h3>Traveling California's Bramble Shore<br>5 Reasons to Move to the West Coast</h3><div class="photo" role="img" aria-label="Large house with a lawn under a blue sky" style="background:linear-gradient(#7fb2e0,#c8b89a 55%,#5e8a3a)"></div><p>Lorem Ipsum is simply dummy text of the printing and typesetting industry. Lorem Ipsum has been the industry's standard dummy text ever since the 1500s, when an unknown printer took a galley of type and scrambled it to make a type specimen book. It has survived not only five centuries, but also the leap into electronic typesetting, remaining essentially unchanged.</p><div class="post-meta"><svg viewBox="0 0 16 16"><path d="M2 2h12v9H6l-4 3z"/></svg>Comments<span class="spacer"></span><svg viewBox="0 0 16 16"><circle cx="12" cy="3" r="2.5"/><circle cx="4" cy="8" r="2.5"/><circle cx="12" cy="13" r="2.5"/><path d="M4 8l8-5M4 8l8 5" stroke="#333" stroke-width="1.3"/></svg>Share<span class="read-more">Read More</span></div></article>
  <article class="post-card"><h3>Traveling California's Bramble Shore<br>5 Reasons to Move to the West Coast</h3><div class="photo" role="img" aria-label="Family standing in front of a new home" style="background:linear-gradient(#9cc4e6,#c9a37a 55%,#6a4a30)"></div><p>Lorem Ipsum is simply dummy text of the printing and typesetting industry. Lorem Ipsum has been the industry's standard dummy text ever since the 1500s, when an unknown printer took a galley of type and scrambled it to make a type specimen book. It has survived not only five centuries, but also the leap into electronic typesetting, remaining essentially unchanged.</p><div class="post-meta"><svg viewBox="0 0 16 16"><path d="M2 2h12v9H6l-4 3z"/></svg>Comments<span class="spacer"></span><svg viewBox="0 0 16 16"><circle cx="12" cy="3" r="2.5"/><circle cx="4" cy="8" r="2.5"/><circle cx="12" cy="13" r="2.5"/><path d="M4 8l8-5M4 8l8 5" stroke="#333" stroke-width="1.3"/></svg>Share<span class="read-more">Read More</span></div></article>
  <article class="post-card"><h3>Traveling California's Bramble Shore<br>5 Reasons to Move to the West Coast</h3><div class="photo" role="img" aria-label="Real estate agent handing over house keys" style="background:linear-gradient(#e8e8e8,#a9a9a9 60%,#4a4a4a)"></div><p>Lorem Ipsum is simply dummy text of the printing and typesetting industry. Lorem Ipsum has been the industry's standard dummy text ever since the 1500s, when an unknown printer took a galley of type and scrambled it to make a type specimen book. It has survived not only five centuries, but also the leap into electronic typesetting, remaining essentially unchanged.</p><div class="post-meta"><svg viewBox="0 0 16 16"><path d="M2 2h12v9H6l-4 3z"/></svg>Comments<span class="spacer"></span><svg viewBox="0 0 16 16"><circle cx="12" cy="3" r="2.5"/><circle cx="4" cy="8" r="2.5"/><circle cx="12" cy="13" r="2.5"/><path d="M4 8l8-5M4 8l8 5" stroke="#333" stroke-width="1.3"/></svg>Share<span class="read-more">Read More</span></div></article>
  <article class="post-card"><h3>Traveling California's Bramble Shore<br>5 Reasons to Move to the West Coast</h3><div class="photo" role="img" aria-label="Pizza with basil and tomatoes on a dark table" style="background:linear-gradient(#a8442a,#6a2a14 60%,#2a140a)"></div><p>Lorem Ipsum is simply dummy text of the printing and typesetting industry. Lorem Ipsum has been the industry's standard dummy text ever since the 1500s, when an unknown printer took a galley of type and scrambled it to make a type specimen book. It has survived not only five centuries, but also the leap into electronic typesetting, remaining essentially unchanged.</p><div class="post-meta"><svg viewBox="0 0 16 16"><path d="M2 2h12v9H6l-4 3z"/></svg>Comments<span class="spacer"></span><svg viewBox="0 0 16 16"><circle cx="12" cy="3" r="2.5"/><circle cx="4" cy="8" r="2.5"/><circle cx="12" cy="13" r="2.5"/><path d="M4 8l8-5M4 8l8 5" stroke="#333" stroke-width="1.3"/></svg>Share<span class="read-more">Read More</span></div></article>
  <article class="post-card"><h3>Traveling California's Bramble Shore<br>5 Reasons to Move to the West Coast</h3><div class="photo" role="img" aria-label="Friends toasting with red wine at a table" style="background:linear-gradient(#d8b890,#8a3a2a 55%,#3a1a10)"></div><p>Lorem Ipsum is simply dummy text of the printing and typesetting industry. Lorem Ipsum has been the industry's standard dummy text ever since the 1500s, when an unknown printer took a galley of type and scrambled it to make a type specimen book. It has survived not only five centuries, but also the leap into electronic typesetting, remaining essentially unchanged.</p><div class="post-meta"><svg viewBox="0 0 16 16"><path d="M2 2h12v9H6l-4 3z"/></svg>Comments<span class="spacer"></span><svg viewBox="0 0 16 16"><circle cx="12" cy="3" r="2.5"/><circle cx="4" cy="8" r="2.5"/><circle cx="12" cy="13" r="2.5"/><path d="M4 8l8-5M4 8l8 5" stroke="#333" stroke-width="1.3"/></svg>Share<span class="read-more">Read More</span></div></article>
  <article class="post-card"><h3>Traveling California's Bramble Shore<br>5 Reasons to Move to the West Coast</h3><div class="photo" role="img" aria-label="Audience at a seminar facing a speaker" style="background:linear-gradient(#eef0f2,#a6a09a 55%,#3e3630)"></div><p>Lorem Ipsum is simply dummy text of the printing and typesetting industry. Lorem Ipsum has been the industry's standard dummy text ever since the 1500s, when an unknown printer took a galley of type and scrambled it to make a type specimen book. It has survived not only five centuries, but also the leap into electronic typesetting, remaining essentially unchanged.</p><div class="post-meta"><svg viewBox="0 0 16 16"><path d="M2 2h12v9H6l-4 3z"/></svg>Comments<span class="spacer"></span><svg viewBox="0 0 16 16"><circle cx="12" cy="3" r="2.5"/><circle cx="4" cy="8" r="2.5"/><circle cx="12" cy="13" r="2.5"/><path d="M4 8l8-5M4 8l8 5" stroke="#333" stroke-width="1.3"/></svg>Share<span class="read-more">Read More</span></div></article>
  <article class="post-card"><h3>Traveling California's Bramble Shore<br>5 Reasons to Move to the West Coast</h3><div class="photo" role="img" aria-label="Pizza slices on a wooden board" style="background:linear-gradient(#e0b070,#b0542a 55%,#5a2a14)"></div><p>Lorem Ipsum is simply dummy text of the printing and typesetting industry. Lorem Ipsum has been the industry's standard dummy text ever since the 1500s, when an unknown printer took a galley of type and scrambled it to make a type specimen book. It has survived not only five centuries, but also the leap into electronic typesetting, remaining essentially unchanged.</p><div class="post-meta"><svg viewBox="0 0 16 16"><path d="M2 2h12v9H6l-4 3z"/></svg>Comments<span class="spacer"></span><svg viewBox="0 0 16 16"><circle cx="12" cy="3" r="2.5"/><circle cx="4" cy="8" r="2.5"/><circle cx="12" cy="13" r="2.5"/><path d="M4 8l8-5M4 8l8 5" stroke="#333" stroke-width="1.3"/></svg>Share<span class="read-more">Read More</span></div></article>
</div>

<div class="abs pagination"><span>‹</span><span>1</span><span>2</span><span>3</span><span class="on">4</span><span>5</span><span>...</span><span>10</span><span>20</span><span>30</span><span>›</span></div>

<div class="abs side-label" style="top:1340px">SPONSORED ADS</div>
<aside class="abs sponsor-slot sponsor-tall" role="img" aria-label="Sponsored advertisement: tall display banner with an outdoor field scene"></aside>

<h2 class="abs section-title recent-heading">RECENT POSTS</h2>
<div class="abs recent-post" style="top:2110px"><div class="photo" role="img" aria-label="Woman sipping coffee from a cup" style="background:linear-gradient(135deg,#f0c8a0,#b06a3a 55%,#3a1a0a)"></div><p>Neque porro quisquam est qui dolorem</p><div class="post-meta"><svg viewBox="0 0 16 16"><path d="M2 2h12v9H6l-4 3z"/></svg>Comments<span class="spacer"></span><svg viewBox="0 0 16 16"><circle cx="12" cy="3" r="2.5"/><circle cx="4" cy="8" r="2.5"/><circle cx="12" cy="13" r="2.5"/><path d="M4 8l8-5M4 8l8 5" stroke="#333" stroke-width="1.3"/></svg>Share</div></div>
<div class="abs recent-post" style="top:2375px"><div class="photo" role="img" aria-label="Bunch of dark grapes on the vine" style="background:linear-gradient(135deg,#6a8a2a,#2a3a4a 55%,#120e1e)"></div><p>Neque porro quisquam est qui dolorem</p><div class="post-meta"><svg viewBox="0 0 16 16"><path d="M2 2h12v9H6l-4 3z"/></svg>Comments<span class="spacer"></span><svg viewBox="0 0 16 16"><circle cx="12" cy="3" r="2.5"/><circle cx="4" cy="8" r="2.5"/><circle cx="12" cy="13" r="2.5"/><path d="M4 8l8-5M4 8l8 5" stroke="#333" stroke-width="1.3"/></svg>Share</div></div>
<div class="abs recent-post" style="top:2640px"><div class="photo" role="img" aria-label="Vineyard rows at sunset" style="background:linear-gradient(#f0b048,#a86a20 45%,#3a3a14)"></div><p>Neque porro quisquam est qui dolorem</p><div class="post-meta"><svg viewBox="0 0 16 16"><path d="M2 2h12v9H6l-4 3z"/></svg>Comments<span class="spacer"></span><svg viewBox="0 0 16 16"><circle cx="12" cy="3" r="2.5"/><circle cx="4" cy="8" r="2.5"/><circle cx="12" cy="13" r="2.5"/><path d="M4 8l8-5M4 8l8 5" stroke="#333" stroke-width="1.3"/></svg>Share</div></div>

<section class="abs newsletter">
  <h4>Sign Up</h4>
  <h5>For Newsletter</h5>
  <p>Lorem Ipsum is simply dummy text of the printing and typesetting industry.</p>
  <div class="email">Enter Your E-mail Address</div>
  <span class="subscribe">SUBSCRIBE</span>
  <small>Get top stories and blog posts emailed to me each day.</small>
</section>

<div class="abs side-label" style="top:3262px">FOLLOW US ON :</div>
<div class="abs social-row"><i></i><i></i><i></i><i></i><i></i><i></i><i></i></div>

<div class="abs side-label" style="top:3368px">SPONSORED ADS</div>
<aside class="abs sponsor-slot sponsor-wide" role="img" aria-label="Sponsored advertisement: event registration banner on a dark background"></aside>

<div class="abs recent-post" style="top:3680px"><div class="photo" role="img" aria-label="Cup of coffee on a saucer" style="background:linear-gradient(#e8e2da,#7a5030 55%,#2a1a10)"></div><p>Neque porro quisquam est qui dolorem</p><div class="post-meta"><svg viewBox="0 0 16 16"><path d="M2 2h12v9H6l-4 3z"/></svg>Comments<span class="spacer"></span><svg viewBox="0 0 16 16"><circle cx="12" cy="3" r="2.5"/><circle cx="4" cy="8" r="2.5"/><circle cx="12" cy="13" r="2.5"/><path d="M4 8l8-5M4 8l8 5" stroke="#333" stroke-width="1.3"/></svg>Share</div></div>
<div class="abs recent-post" style="top:3945px"><div class="photo" role="img" aria-label="Plated meal on a white dish" style="background:linear-gradient(#f4f0ea,#c89a6a 55%,#6a4020)"></div><p>Neque porro quisquam est qui dolorem</p><div class="post-meta"><svg viewBox="0 0 16 16"><path d="M2 2h12v9H6l-4 3z"/></svg>Comments<span class="spacer"></span><svg viewBox="0 0 16 16"><circle cx="12" cy="3" r="2.5"/><circle cx="4" cy="8" r="2.5"/><circle cx="12" cy="13" r="2.5"/><path d="M4 8l8-5M4 8l8 5" stroke="#333" stroke-width="1.3"/></svg>Share</div></div>
<div class="abs recent-post" style="top:4210px"><div class="photo" role="img" aria-label="Friends sharing a meal at a restaurant" style="background:linear-gradient(#e0c8a8,#a07050 55%,#4a2a18)"></div><p>Neque porro quisquam est qui dolorem</p><div class="post-meta"><svg viewBox="0 0 16 16"><path d="M2 2h12v9H6l-4 3z"/></svg>Comments<span class="spacer"></span><svg viewBox="0 0 16 16"><circle cx="12" cy="3" r="2.5"/><circle cx="4" cy="8" r="2.5"/><circle cx="12" cy="13" r="2.5"/><path d="M4 8l8-5M4 8l8 5" stroke="#333" stroke-width="1.3"/></svg>Share</div></div>
<div class="abs recent-post" style="top:4480px"><div class="photo" role="img" aria-label="Restaurant dining room with set tables" style="background:linear-gradient(#9a8a7a,#4a3a30 55%,#1a1410)"></div><p>Neque porro quisquam est qui dolorem</p><div class="post-meta"><svg viewBox="0 0 16 16"><path d="M2 2h12v9H6l-4 3z"/></svg>Comments<span class="spacer"></span><svg viewBox="0 0 16 16"><circle cx="12" cy="3" r="2.5"/><circle cx="4" cy="8" r="2.5"/><circle cx="12" cy="13" r="2.5"/><path d="M4 8l8-5M4 8l8 5" stroke="#333" stroke-width="1.3"/></svg>Share</div></div>

<footer class="abs site-footer">
  <nav><span>LODGING</span><span>DINING</span><span>WINERIES</span><span>ACTIVITIES &amp; EVENTS</span><span>REAL ESTATE</span><span>FOR SALE</span><span>AUTO</span><span>SHOPPING</span><span>JOBS</span></nav>
  <div class="copy">COPYRIGHT © 2015 COMPANY NAME | ALL RIGHTS RESERVED.</div>
  <div class="mark">BS</div>
</footer>

</body>
</html>
```